Dog Coat Drive for San Francisco Homeless Pets

- one page, full color, flyer to advertise a winter dog coat drive.- requesting use of an image of pit bull type or chihuahua type dog in a coat - 2 size versions - 8.5 inch by 11 inch to be printed and a square design to be posted on FB, Instagram and websites

Font styles to use
Serif
Sans Serif

Colors

Designer to choose colors to be used in the design.

```html
<!DOCTYPE html>
<html lang="en">
<head>
<meta charset="utf-8">
<title>Dog Coat Drive Flyer</title>
<link rel="stylesheet" href="https://fonts.googleapis.com/css2?family=Arimo:wght@400;600;700&family=Nunito:wght@800;900&display=swap">
<style>
  :root {
    --sky: #3db3e8;
    --sky-deep: #1f9bd8;
    --frost: #cfe9f8;
    --frost-light: #eef7fd;
    --ink: #2b2b2b;
    --white: #ffffff;
    --coat-brown: #b89272;
    --coat-cream: #ede5d6;
    --coat-green: #8fcf5a;
  }
  * { margin: 0; padding: 0; box-sizing: border-box; }
  html, body { width: 1002px; height: 1200px; overflow: hidden; background: var(--white); }
  .flyer {
    position: relative; width: 1002px; height: 1200px; overflow: hidden;
    font-family: "Arimo", Arial, sans-serif; color: var(--ink);
    background: linear-gradient(180deg, var(--frost-light) 0%, var(--frost) 55%, var(--white) 74%, var(--white) 100%);
  }
  .lower-band { position: absolute; left: 0; top: 895px; width: 1002px; height: 305px; background: var(--white); }
  .brand-circle {
    position: absolute; left: -90px; top: -180px; width: 700px; height: 700px;
    border-radius: 50%; background: var(--white);
  }
  .brand { position: absolute; left: 50px; top: 180px; width: 420px; text-align: center; }
  .brand-mark { display: block; width: 70px; height: 70px; margin: 0 auto 26px; border-radius: 50%; background: var(--sky); }
  .brand-name { font-size: 40px; font-weight: 700; color: var(--ink); line-height: 1.05; }
  .brand-tag { font-size: 21px; font-weight: 600; margin-top: 10px; color: var(--ink); }

  .headline-panel {
    position: absolute; left: 511px; top: 50px; width: 452px; height: 741px;
    background: var(--sky); border-radius: 30px;
  }
  .headline { position: absolute; left: 511px; top: 82px; width: 452px; text-align: center;
    font-family: "Nunito", Arial, sans-serif; font-weight: 900; color: var(--white);
    text-shadow: 0 0 6px var(--sky-deep), 0 3px 0 var(--sky-deep); }
  .headline .big { font-size: 112px; line-height: 114px; letter-spacing: 1px; }
  .headline .mid { font-size: 70px; line-height: 88px; }
  .drive-title { position: absolute; left: 511px; top: 418px; width: 452px; text-align: center;
    color: var(--white); font-weight: 700; font-size: 29px; line-height: 45px; }

  .photo { position: absolute; }
  .photo-chihuahua-large { left: 40px; top: 450px; width: 390px; height: 440px; border-radius: 46% 46% 18% 18%;
    background: linear-gradient(180deg, #c9a883 0%, var(--coat-cream) 45%, var(--coat-brown) 100%); }
  .photo-chihuahua-small { left: 400px; top: 600px; width: 200px; height: 260px; border-radius: 45% 45% 14% 14%;
    background: linear-gradient(180deg, #c99a6e 0%, #3a3a3a 70%, #d8c4ae 100%); }
  .photo-pitbull { left: 590px; top: 580px; width: 376px; height: 295px; border-radius: 40% 30% 14% 14%;
    background: linear-gradient(135deg, #a7714f 0%, var(--coat-green) 55%, #e9e4dc 100%); }

  .appeal { position: absolute; left: 40px; top: 952px; width: 350px; text-align: center;
    font-size: 17px; font-weight: 600; line-height: 34px; letter-spacing: 0.3px; text-transform: uppercase; color: #333; }
  .divider { position: absolute; left: 416px; top: 938px; width: 1px; height: 233px; background: var(--sky); }

  .partner { position: absolute; width: 200px; text-align: center; font-size: 13px; font-weight: 600; line-height: 18px; color: #222; }
  .partner-name { display: flex; align-items: center; justify-content: center; gap: 6px; height: 58px;
    font-size: 14px; font-weight: 700; color: var(--sky-deep); margin-bottom: 10px; }
  .partner-dot { width: 14px; height: 14px; border-radius: 50%; background: var(--sky-deep); flex: none; }
  .row-one { top: 935px; }
  .row-two { top: 1058px; }
</style>
</head>
<body>
<main class="flyer">
  <div class="lower-band"></div>
  <div class="brand-circle"></div>

  <header class="brand">
    <span class="brand-mark"></span>
    <div class="brand-name">Warm Paws Outreach</div>
    <div class="brand-tag">Neighborhood Pet Help</div>
  </header>

  <div class="headline-panel"></div>
  <h1 class="headline">
    <div class="big">BABY,</div>
    <div class="mid">It’s Cold</div>
    <div class="mid">Outside!</div>
  </h1>
  <h2 class="drive-title">DOG COAT DRIVE<br>FOR SF<br>NAVIGATION CENTERS</h2>

  <div class="photo photo-chihuahua-large" role="img" aria-label="Photo of a chihuahua wearing a cream polka-dot coat"></div>
  <div class="photo photo-chihuahua-small" role="img" aria-label="Photo of a small chihuahua in a black sweater"></div>
  <div class="photo photo-pitbull" role="img" aria-label="Photo of a pit bull type dog wearing a green winter coat"></div>

  <p class="appeal">Please donate new &amp; gently<br>used dog coats, sweaters<br>and jackets for navigation<br>center dogs whose owners<br>are working to prevent and<br>end their homelessness</p>
  <div class="divider"></div>

  <section class="partners">
    <div class="partner row-one" style="left:419px">
      <div class="partner-name"><span class="partner-dot"></span>Harbor Animal Services</div>
      2410 Larch Street<br>415-555-0142
    </div>
    <div class="partner row-one" style="left:602px">
      <div class="partner-name"><span class="partner-dot"></span>Bright Tail Pet Care</div>
      76 Shoreline Way, Pacifica<br>650-555-0187
    </div>
    <div class="partner row-one" style="left:794px">
      <div class="partner-name"><span class="partner-dot"></span>Cedar Pet Supply</div>
      1830 Maple Street<br>415-555-0126
    </div>
    <div class="partner row-two" style="left:487px">
      <div class="partner-name"><span class="partner-dot"></span>The Kennel Corner</div>
      342 Alder Street<br>415-555-0163
    </div>
    <div class="partner row-two" style="left:708px">
      <div class="partner-name"><span class="partner-dot"></span>Baywood Pet Hub</div>
      905 Seabreeze Ave, Pacifica<br>650-555-0178
    </div>
  </section>
</main>
</body>
</html>
```